Bref créative
Limb Nestler
Naturally made in the US
Professional
Rosalind Featherstone
Owner
437 Tamsin Ave - Ste 220-581
rfeatherstone@limbnestler-example.com
Limbnestler-example.com
I'm not sure what the first two boxes refer to. I want our logo to be on the cards in the same colors.

```html
<!DOCTYPE html>
<html lang="en">
<head>
<meta charset="utf-8">
<title>Limb Nestler — Stationery Set</title>
<link href="https://fonts.googleapis.com/css2?family=Open+Sans:wght@400;600;700&display=swap" rel="stylesheet">
<style>
  :root{
    --blue:#1e8fd5;
    --maroon:#7a1f25;
    --ink:#151515;
    --text:#4a4a4a;
    --muted:#8a8a8a;
    --paper:#ffffff;
    --stage:#e8e6e2;
    --rule:#d6d6d6;
  }
  *{box-sizing:border-box;margin:0;padding:0}
  html,body{width:1200px;height:721px;overflow:hidden}
  body{background:var(--stage);font-family:"Open Sans",Arial,sans-serif;color:var(--text);position:relative}
  .sheet{position:absolute;background:var(--paper);overflow:hidden}

  /* brand lockup */
  .brand{display:flex;align-items:center;gap:6px}
  .brand-dot{width:14px;height:14px;border-radius:50%;background:var(--blue);flex:none}
  .brand-name{font-weight:600;color:var(--maroon);font-size:15px;line-height:1;white-space:nowrap}
  .brand-tag{display:block;font-size:5px;color:var(--muted);margin-top:2px;letter-spacing:.3px}
  .brand.on-dark .brand-name{color:#fff}
  .brand.on-dark .brand-dot{background:#fff}
  .brand.centered{justify-content:center}

  /* business cards */
  .card{top:53px;width:180px;height:98px;display:flex;align-items:center;justify-content:center}
  .card.front-white{left:62px;display:block}
  .card.blue{left:266px;background:var(--blue)}
  .card.maroon{left:458px;background:var(--maroon)}
  .card.black{left:650px;background:var(--ink)}
  .card.white{left:842px}
  .card .url{position:absolute;bottom:8px;left:0;right:0;text-align:center;font-size:6px;color:#fff;letter-spacing:.4px}
  .card.white .url{color:var(--maroon)}
  .card .brand-dot{background:#fff}
  .card.white .brand-dot,.card.front-white .brand-dot{background:var(--blue)}
  .card.blue .brand-name,.card.maroon .brand-name,.card.black .brand-name{color:#fff}
  .card-logo{position:absolute;left:12px;top:12px}
  .card-logo .brand-dot{width:11px;height:11px}
  .card-logo .brand-name{font-size:11px}
  .card-person{position:absolute;left:100px;top:40px;font-size:5.5px;line-height:1.5;white-space:nowrap}
  .card-person strong{display:block;font-size:6.5px;color:var(--maroon);font-weight:700}
  .card-contact{position:absolute;left:12px;top:60px;font-size:5px;line-height:1.5;color:var(--text);white-space:nowrap}

  /* compliment slip */
  .slip{left:62px;top:180px;width:346px;height:156px;padding:18px 20px}
  .slip-footer{position:absolute;left:20px;bottom:14px;font-size:5.5px;line-height:1.6;color:var(--text)}

  /* envelope */
  .envelope{left:62px;top:365px;width:351px;height:326px;background:transparent;overflow:visible}
  .env-flap{position:absolute;left:0;top:0;width:351px;height:120px;background:var(--paper)}
  .env-flap svg{position:absolute;inset:0}
  .env-flap .brand{position:absolute;left:0;right:0;top:44px}
  .env-band{position:absolute;left:0;width:351px;height:96px;display:flex;align-items:center;justify-content:center}
  .env-band.blue{top:126px;background:var(--blue)}
  .env-band.maroon{top:228px;background:var(--maroon)}
  .env-band .url{position:absolute;bottom:6px;right:12px;font-size:5.5px;color:#fff}

  /* letterhead */
  .letterhead{left:437px;top:180px;width:331px;height:516px;padding:22px 26px}
  .letter-recipient{margin-top:26px;font-size:5.5px;line-height:1.5}
  .letter-body{margin-top:12px;font-size:5.5px;line-height:1.6;color:var(--text)}
  .letter-body p{margin-bottom:8px}
  .signature{display:block;width:60px;height:18px;margin:6px 0 4px;background:linear-gradient(90deg,#e9eef3,#f6f8fa)}
  .letter-footer{position:absolute;left:26px;right:26px;bottom:16px;border-top:1px solid var(--rule);padding-top:6px;display:flex;justify-content:space-between;font-size:5.5px;color:var(--maroon)}
  .letter-footer span:last-child{color:var(--blue)}

  /* fax */
  .fax{left:797px;top:180px;width:341px;height:516px;padding:22px 22px}
  .fax-title{position:absolute;right:24px;top:70px;font-size:16px;font-weight:600;color:var(--ink);letter-spacing:1px}
  .fax-rule{position:absolute;left:22px;right:22px;top:92px;height:2px;background:var(--maroon)}
  .fax-grid{position:absolute;left:22px;right:22px;top:100px;display:grid;grid-template-columns:34px 1fr 34px 1fr;gap:3px 4px;font-size:5.5px}
  .fax-grid .label{padding:3px 0;color:var(--text)}
  .fax-grid .field{height:12px;background:#eef1f4;border:1px solid #dfe3e8}
  .fax-checks{position:absolute;left:22px;right:22px;top:188px;display:flex;justify-content:space-between;font-size:5.5px}
  .fax-checks span{display:flex;align-items:center;gap:3px}
  .fax-checks i{width:6px;height:6px;border:1px solid var(--muted);display:inline-block}
  .fax-comments{position:absolute;left:22px;top:206px;font-size:5.5px}
</style>
</head>
<body>

  <!-- Business cards -->
  <div class="sheet card front-white">
    <div class="brand card-logo">
      <span class="brand-dot"></span>
      <span><span class="brand-name">Limb Nestler</span><span class="brand-tag">Naturally made in the US</span></span>
    </div>
    <div class="card-person"><strong>Rosalind Featherstone</strong>Owner</div>
    <div class="card-contact">
      437 Tamsin Ave - Ste 220-581<br>
      T: 555 014 2287<br>
      rfeatherstone@limbnestler-example.com<br>
      Limbnestler-example.com
    </div>
  </div>
  <div class="sheet card blue">
    <div class="brand"><span class="brand-dot"></span><span class="brand-name">Limb Nestler</span></div>
    <span class="url">www.Limbnestler-example.com</span>
  </div>
  <div class="sheet card maroon">
    <div class="brand"><span class="brand-dot"></span><span class="brand-name">Limb Nestler</span></div>
    <span class="url">www.Limbnestler-example.com</span>
  </div>
  <div class="sheet card black">
    <div class="brand"><span class="brand-dot"></span><span class="brand-name">Limb Nestler</span></div>
    <span class="url">www.Limbnestler-example.com</span>
  </div>
  <div class="sheet card white">
    <div class="brand"><span class="brand-dot"></span><span class="brand-name">Limb Nestler</span></div>
    <span class="url">www.Limbnestler-example.com</span>
  </div>

  <!-- Compliment slip -->
  <div class="sheet slip">
    <div class="brand">
      <span class="brand-dot"></span>
      <span><span class="brand-name">Limb Nestler</span><span class="brand-tag">Naturally made in the US</span></span>
    </div>
    <div class="slip-footer">
      437 Tamsin Ave - Ste 220-581<br>
      T: 555 014 2287<br>
      Limbnestler-example.com
    </div>
  </div>

  <!-- Envelope -->
  <div class="sheet envelope">
    <div class="env-flap">
      <svg width="351" height="120" viewBox="0 0 351 120">
        <polyline points="0,0 175,34 351,0" fill="none" stroke="#d0d0d0" stroke-width="1"/>
      </svg>
      <div class="brand centered"><span class="brand-dot"></span><span class="brand-name">Limb Nestler</span></div>
    </div>
    <div class="env-band blue">
      <div class="brand on-dark"><span class="brand-dot"></span><span class="brand-name">Limb Nestler</span></div>
    </div>
    <div class="env-band maroon">
      <div class="brand on-dark"><span class="brand-dot"></span><span class="brand-name">Limb Nestler</span></div>
      <span class="url">Limbnestler-example.com</span>
    </div>
  </div>

  <!-- Letterhead -->
  <div class="sheet letterhead">
    <div class="brand">
      <span class="brand-dot"></span>
      <span><span class="brand-name">Limb Nestler</span><span class="brand-tag">Naturally made in the US</span></span>
    </div>
    <div class="letter-recipient">
      Marcus Whitfield<br>12 Orchard Lane<br>Fairbrook, Oregon
    </div>
    <div class="letter-body">
      <p>Dear Marcus Whitfield,</p>
      <p>Thank you for your recent interest in our handmade comfort pillows. We are glad to share our full range of support cushions, each one sewn with care in our own workshop using soft natural fabrics and clean organic fill.</p>
      <p>Every piece is shaped to cradle the neck, back and limbs so that rest comes easily at home, at work or on the road. Our team tests each design for weeks before it ever reaches a customer.</p>
      <p>Please find our current price list enclosed. We would be happy to arrange a sample set for your store and to answer any questions you may have.</p>
      <p>Kind regards,</p>
      <span class="signature" role="img" aria-label="Handwritten signature of rfeathst"></span>
      <p>Rosalind Featherstone<br>Owner</p>
    </div>
    <div class="letter-footer">
      <span>437 Tamsin Ave - Ste 220-581 · T: 555 014 2287</span>
      <span>Limbnestler-example.com</span>
    </div>
  </div>

  <!-- Fax cover -->
  <div class="sheet fax">
    <div class="brand">
      <span class="brand-dot"></span>
      <span><span class="brand-name">Limb Nestler</span><span class="brand-tag">Naturally made in the US</span></span>
    </div>
    <div class="fax-title">FAX</div>
    <div class="fax-rule"></div>
    <div class="fax-grid">
      <span class="label">To:</span><span class="field"></span><span class="label">From:</span><span class="field"></span>
      <span class="label">Fax:</span><span class="field"></span><span class="label">Pages:</span><span class="field"></span>
      <span class="label">Phone:</span><span class="field"></span><span class="label">Date:</span><span class="field"></span>
      <span class="label">Re:</span><span class="field"></span><span class="label">CC:</span><span class="field"></span>
    </div>
    <div class="fax-checks">
      <span><i></i>Urgent</span>
      <span><i></i>For Review</span>
      <span><i></i>Please Comment</span>
      <span><i></i>Please Reply</span>
      <span><i></i>Please Recycle</span>
    </div>
    <div class="fax-comments">Comments:</div>
  </div>

</body>
</html>
```